Need a book cover design for a Lumora Book on Herbal Remedies

I need a book cover for my new ebook, here are the details:
Title: Meadow Cures
Sub-Heading: Buried Ancient Garden Tonics
Reclaiming the Wisdom of Roots for Everyday Wellness and Strength
Author: Nora Belcourt

```html
<!DOCTYPE html>
<html lang="en">
<head>
<meta charset="utf-8">
<title>Meadow Cures — Nora Belcourt</title>
<link rel="stylesheet" href="https://fonts.googleapis.com/css2?family=Source+Serif+4:ital,opsz,wght@0,8..60,600;0,8..60,700;1,8..60,400&family=Source+Sans+3:wght@400&display=swap">
<style>
  :root {
    --page: #fefdf0;
    --leaf-deep: #6f8a2a;
    --leaf-light: #8fb03a;
    --ring-orange: #ee8a2a;
    --ring-yellow: #f4b62c;
    --core-red: #d0203c;
    --title-white: #ffffff;
    --subtitle-yellow: #f7e62a;
  }
  html, body {
    margin: 0;
    width: 1200px;
    height: 1000px;
    overflow: hidden;
    background: var(--page);
  }
  .canvas {
    position: relative;
    width: 1200px;
    height: 1000px;
  }
  .cover {
    position: absolute;
    left: 310px;
    top: 36px;
    width: 580px;
    height: 928px;
    overflow: hidden;
    background: var(--leaf-deep);
  }
  .cover-foliage {
    position: absolute;
    inset: 0;
    background:
      radial-gradient(ellipse at 20% 15%, rgba(143,176,58,.7), transparent 45%),
      radial-gradient(ellipse at 80% 85%, rgba(143,176,58,.6), transparent 45%),
      linear-gradient(160deg, var(--leaf-light), var(--leaf-deep) 55%, var(--leaf-light));
  }
  .sun-ring {
    position: absolute;
    left: -70px;
    top: 84px;
    width: 720px;
    height: 720px;
    border-radius: 50%;
    background: radial-gradient(circle, var(--ring-orange) 55%, var(--ring-yellow) 80%, #c9a035 100%);
  }
  .sun-core {
    position: absolute;
    left: 18px;
    top: 172px;
    width: 544px;
    height: 544px;
    border-radius: 50%;
    background: var(--core-red);
  }
  .cover-text {
    position: absolute;
    left: 0;
    width: 580px;
    text-align: center;
    margin: 0;
  }
  .title {
    top: 176px;
    font-family: "Source Serif 4", Georgia, serif;
    font-weight: 600;
    font-size: 92px;
    line-height: 96px;
    color: var(--title-white);
    letter-spacing: 0.5px;
  }
  .subtitle {
    top: 414px;
    font-family: "Source Serif 4", Georgia, serif;
    font-style: italic;
    font-weight: 400;
    font-size: 37px;
    line-height: 44px;
    color: var(--subtitle-yellow);
  }
  .tagline {
    top: 491px;
    font-family: "Source Sans 3", Arial, sans-serif;
    font-size: 21px;
    line-height: 28px;
    color: var(--title-white);
  }
  .divider-sprig {
    position: absolute;
    left: 282px;
    top: 585px;
    width: 18px;
    height: 11px;
    border-radius: 50%;
    background: var(--title-white);
    opacity: .85;
  }
  .author {
    top: 620px;
    font-family: "Source Serif 4", Georgia, serif;
    font-weight: 700;
    font-size: 19px;
    line-height: 26px;
    color: var(--title-white);
  }
</style>
</head>
<body>
<div class="canvas">
  <section class="cover">
    <div class="cover-foliage" role="img" aria-label="Green background of overlapping stylised leaves"></div>
    <div class="sun-ring" role="img" aria-label="Glowing orange and yellow ring with leaf texture"></div>
    <div class="sun-core"></div>
    <h1 class="cover-text title">Meadow<br>Cures</h1>
    <p class="cover-text subtitle">Buried Ancient Garden Tonics</p>
    <p class="cover-text tagline">Reclaiming the Wisdom of Roots<br>for Everyday Wellness and Strength</p>
    <div class="divider-sprig" role="img" aria-label="Small leaf sprig ornament"></div>
    <p class="cover-text author">Author: Nora Belcourt</p>
  </section>
</div>
</body>
</html>
```